Swimming Pool Service Website needed!!!

Hi Everyone! Thanks for looking at my contest. I PROMISE to provide excellent feedback during this process.

I am starting a new swimming pool business cleaning company in San Diego, California and would like your help in making it similar to one of these two websites that are already functioning.

http://www.brightlagoonworks.example/services-repair.html

http://tidemarkaquacare.example/commercial-pool-cleaning.php

I like these two because they are easy to read, classy, sophisticated and have nice pictures of really clean & clear pools.

I really like the blue on white color format.

I do not have a logo, but the name of my company is GLIMMERWAVE POOL SERVICE.

My tag line is: Water so pure, it sparkles like a summer sky. (does not need to have the quotes around "in"...maybe just italics for this word IN?) You decide for me.

I would like to have a logo designed that incorporates some sort of easy to read letters. I do not want cursive (handwriting) letters. I thought about having a "reflection" of letters (mirror image), but think that this will be hard to read from far away. Maybe you can surprise me and come up with an idea that works using the a mirror image....but I'm not sure. I was leaning toward plain old BLOCK letters as I think it would be easy to read on my truck.

I would like to have 5 pages on my website:
1) Home
2) About Us (Know Your Poolman) / Why Hire Us
3) Services Offered
4) FAQ's
5) Contact

I am looking for a fully-functioning website (coded). Upon selection of the design winner, I am offering to increase the budget/payment by $100-$125 for the coding of all the pages. So anyone looking at participating in this contest, should be willing and able to provide the coding to the webpages that i've requested.

Target Market(s)

Upper middle-class homeowners who have a pool

Industry/Entity Type

Pool Service

Number of Pages Required

5+ page

Font styles to use
Serif

Colors
0455a3
3276b5
85acd3
85cae6
ffffff
33a6d7
0592cd

Requirements
Must have
• The Home page must have this picture highlighted in the top of the page:
• http://www.mesawaterpro.example/
• Must have pictures of some high-end pools. Any that you can find on the internet are wonderful.
• Must have a table on the right of the home page that mentions the service areas that we go to:
• • Carmel Valley (92130)
• • Del Mar (92014)
• • Rancho Santa Fe (92067)
• • Solana Beach (92075)
• • Santaluz (92127)
• • Cardiff (92007)
• • Encinitas (92024)
• • Carlsbad (92009, 92008)
• • La Jolla (92037)
• • Pacific Beach (92109)
• • Mira Mesa (92126)
• • Sorrento Valley (92121)
• • Clairemont (92117)
• • Rancho Bernardo (92127, 92128)
• • Rancho Penasquitos (92129)
• • Poway (92064)
• •
Nice to have
• Maybe incorporate some pictures of some kids (or families) playing in pools on the Why Hire Us page?
• I also like the feel of this website, but posting this page just for reference so you can get a feel more of what I like:
• http://www.crestlinepool.example/
• I like the FAQ's page from this website. I like how you can click on the question and then it pops up with the answer. http://www.dunewoodpoolcare.example/pool-spa-fountain-faqs/

```html
<!DOCTYPE html>
<html lang="en">
<head>
<meta charset="utf-8">
<title>Glimmerwave Pool Service</title>
<link href="https://fonts.googleapis.com/css2?family=Barlow:wght@300;400;500;600&display=swap" rel="stylesheet">
<style>
  :root {
    --navy: #0455a3;
    --blue: #0592cd;
    --sky: #33a6d7;
    --band: #85cae6;
    --white: #ffffff;
    --ink: #333333;
    --muted: #6f6f6f;
    --soft: #9a9a9a;
    --rule: #e4e4e4;
  }
  * { box-sizing: border-box; margin: 0; padding: 0; }
  html, body { width: 685px; height: 1200px; overflow: hidden; }
  body { position: relative; background: var(--white); font-family: "Barlow", Arial, sans-serif; color: var(--ink); }
  .abs { position: absolute; }

  /* Header */
  .site-header { left: 0; top: 0; width: 685px; height: 32px; background: var(--white); }
  .brand { left: 48px; top: 11px; font-size: 11.5px; font-weight: 600; letter-spacing: .6px; color: var(--navy); }
  .main-nav { right: 49px; top: 13px; display: flex; gap: 24px; font-size: 8.5px; color: #555; }
  .main-nav .is-active { color: var(--blue); }

  .hero { left: 0; top: 32px; width: 685px; height: 235px;
    background: linear-gradient(180deg, #6fb4e4 0%, #a9d6f0 28%, #2f86c9 44%, #1377c2 62%, #3aa1db 82%, #7cc4e8 100%); }

  /* Features */
  .feature { top: 285px; width: 180px; }
  .feature .icon { position: absolute; left: 0; top: 0; width: 43px; height: 43px; border-radius: 50%; background: var(--blue); }
  .feature h3 { position: absolute; left: 53px; top: 4px; font-size: 11.5px; font-weight: 400; color: #444; }
  .feature p { position: absolute; left: 53px; top: 23px; width: 125px; font-size: 7.3px; line-height: 1.5; color: var(--muted); }
  .divider { left: 0; top: 357px; width: 685px; height: 1px; background: var(--rule); }

  /* Services */
  .section-title { font-size: 11px; font-weight: 500; color: #333; }
  .services-intro { left: 99px; top: 410px; width: 248px; font-size: 7px; line-height: 1.6; color: var(--soft); }
  .checklist { left: 96px; top: 467px; list-style: none; }
  .checklist li { display: flex; align-items: center; height: 22.5px; font-size: 8px; color: var(--muted); }
  .checklist svg { margin-right: 6px; }
  .areas-list { left: 452px; top: 411px; list-style: none; }
  .areas-list li { height: 12.2px; font-size: 6.4px; color: var(--muted); }
  .areas-list li::before { content: "•"; margin-right: 3px; color: var(--soft); }

  /* Latest work */
  .work-band { left: 0; top: 624px; width: 685px; height: 272px; background: var(--band); }
  .work-title { left: 0; top: 640px; width: 685px; text-align: center; font-size: 14px; font-weight: 400; color: var(--white); }
  .work-card { top: 667px; width: 172px; height: 198px; background: var(--white); }
  .work-card .photo { height: 128px; }
  .work-card h4 { margin-top: 7px; text-align: center; font-size: 11px; font-weight: 400; color: #444; }
  .work-card p { margin: 5px 10px 0; text-align: center; font-size: 7px; line-height: 1.45; color: var(--muted); }

  /* Video + contact */
  .video-title { left: 48px; top: 914px; font-size: 8.5px; font-weight: 600; color: #222; }
  .video-rule { left: 48px; top: 930px; width: 325px; height: 1px; background: var(--rule); }
  .video { left: 48px; top: 940px; width: 325px; height: 200px; border: 3px solid #d9d9d9; }
  .video .frame { position: absolute; inset: 0; background: linear-gradient(180deg, #6e7c69 0%, #8a8f80 30%, #3f9fcf 55%, #1e86c4 80%, #59b3de 100%); }
  .video .controls { position: absolute; left: 0; bottom: 0; width: 100%; height: 14px; background: #1b1b1b; }
  .video .progress { position: absolute; left: 0; bottom: 14px; width: 100%; height: 3px; background: #555; }
  .video .play { position: absolute; left: 140px; top: 78px; }

  .contact-title { left: 421px; top: 912px; font-size: 13px; font-weight: 500; color: #222; }
  .field-label { left: 421px; font-size: 6.5px; color: var(--soft); }
  .field { left: 421px; width: 215px; height: 21px; border: 1px solid #dcdcdc; background: var(--white); }
  .field.is-tall { height: 45px; }
  .send { left: 423px; top: 1117px; width: 77px; height: 26px; background: #19aef0; color: var(--white); font-size: 9.5px; font-weight: 500; display: flex; align-items: center; justify-content: center; }

  /* Footer */
  .site-footer { left: 0; top: 1160px; width: 685px; height: 40px; background: var(--band); }
  .copyright { left: 48px; top: 1176px; font-size: 6.5px; color: var(--white); }
  .social { right: 48px; top: 1173px; display: flex; gap: 5px; }
  .social span { width: 14px; height: 14px; border-radius: 50%; background: var(--white); }
</style>
</head>
<body>

<header class="site-header abs">
  <div class="brand abs">GLIMMERWAVE POOL SERVICE</div>
  <nav class="main-nav abs">
    <span class="is-active">Home</span><span>About Us</span><span>Services</span><span>FAQ</span><span>Why Hire us</span><span>Contact us</span>
  </nav>
</header>

<div class="hero abs" role="img" aria-label="Resort infinity pool with loungers, umbrellas and palm trees by the sea"></div>

<section>
  <div class="feature abs" style="left:49px">
    <div class="icon">
      <svg width="43" height="43" viewBox="0 0 43 43"><g stroke="#fff" stroke-width="3" stroke-linecap="round"><line x1="14" y1="14" x2="29" y2="29"/><line x1="29" y1="14" x2="14" y2="29"/></g><circle cx="13" cy="13" r="3.5" fill="#fff"/><circle cx="30" cy="13" r="3.5" fill="#fff"/></svg>
    </div>
    <h3>Maintenance</h3>
    <p>Lorem Ipsum is simply dummy text of the printing and typesetting industry. Lorem Ipsum has been</p>
  </div>
  <div class="feature abs" style="left:256px">
    <div class="icon">
      <svg width="43" height="43" viewBox="0 0 43 43"><g stroke="#fff" stroke-width="4"><line x1="21.5" y1="10" x2="21.5" y2="33"/><line x1="10" y1="21.5" x2="33" y2="21.5"/><line x1="13.4" y1="13.4" x2="29.6" y2="29.6"/><line x1="29.6" y1="13.4" x2="13.4" y2="29.6"/></g><circle cx="21.5" cy="21.5" r="8" fill="#fff"/><circle cx="21.5" cy="21.5" r="3.5" fill="#0592cd"/></svg>
    </div>
    <h3>Repair</h3>
    <p>Lorem Ipsum is simply dummy text of the printing and typesetting industry. Lorem Ipsum has been</p>
  </div>
  <div class="feature abs" style="left:461px">
    <div class="icon">
      <svg width="43" height="43" viewBox="0 0 43 43"><g stroke="#fff" stroke-width="3" stroke-linecap="round"><line x1="14" y1="14" x2="29" y2="29"/><line x1="29" y1="14" x2="14" y2="29"/></g><circle cx="13" cy="13" r="3.5" fill="#fff"/><circle cx="30" cy="13" r="3.5" fill="#fff"/></svg>
    </div>
    <h3>Maintenance</h3>
    <p>Lorem Ipsum is simply dummy text of the printing and typesetting industry. Lorem Ipsum has been</p>
  </div>
</section>
<div class="divider abs"></div>

<section>
  <h2 class="section-title abs" style="left:99px;top:385px">Services Offered</h2>
  <p class="services-intro abs">Glimmerwave Pool Service is a full service company. We cover the complete spectrum of regular service and repair. From start-ups to restoring swampy pools, repairing or replacing equipment, Glimmerwave does it all.</p>
  <ul class="checklist abs">
    <li><svg width="14" height="14" viewBox="0 0 14 14"><circle cx="7" cy="7" r="7" fill="#19aef0"/><path d="M3.8 7.2l2.2 2.2 4.2-4.6" stroke="#fff" stroke-width="1.6" fill="none"/></svg>Swimming Pool and Spa Cleaning</li>
    <li><svg width="14" height="14" viewBox="0 0 14 14"><circle cx="7" cy="7" r="7" fill="#19aef0"/><path d="M3.8 7.2l2.2 2.2 4.2-4.6" stroke="#fff" stroke-width="1.6" fill="none"/></svg>Install and repair lighting</li>
    <li><svg width="14" height="14" viewBox="0 0 14 14"><circle cx="7" cy="7" r="7" fill="#19aef0"/><path d="M3.8 7.2l2.2 2.2 4.2-4.6" stroke="#fff" stroke-width="1.6" fill="none"/></svg>New Pool and Spa Start Ups</li>
    <li><svg width="14" height="14" viewBox="0 0 14 14"><circle cx="7" cy="7" r="7" fill="#19aef0"/><path d="M3.8 7.2l2.2 2.2 4.2-4.6" stroke="#fff" stroke-width="1.6" fill="none"/></svg>Vacuuming pool floor and steps</li>
    <li><svg width="14" height="14" viewBox="0 0 14 14"><circle cx="7" cy="7" r="7" fill="#19aef0"/><path d="M3.8 7.2l2.2 2.2 4.2-4.6" stroke="#fff" stroke-width="1.6" fill="none"/></svg>Eliminating leaves and debris</li>
    <li><svg width="14" height="14" viewBox="0 0 14 14"><circle cx="7" cy="7" r="7" fill="#19aef0"/><path d="M3.8 7.2l2.2 2.2 4.2-4.6" stroke="#fff" stroke-width="1.6" fill="none"/></svg>Salt water system maintenance</li>
  </ul>

  <h2 class="section-title abs" style="left:447px;top:385px;display:flex;align-items:center">
    <svg width="8" height="11" viewBox="0 0 8 11" style="margin-right:5px"><path d="M4 0C1.8 0 0 1.7 0 3.9 0 6.7 4 11 4 11s4-4.3 4-7.1C8 1.7 6.2 0 4 0z" fill="#333"/><circle cx="4" cy="3.9" r="1.5" fill="#fff"/></svg>Areas We Serve
  </h2>
  <ul class="areas-list abs">
    <li>Carmel Valley (92130)</li><li>Del Mar (92014)</li><li>Rancho Santa Fe (92067)</li><li>Solana Beach (92075)</li>
    <li>Santaluz (92127)</li><li>Cardiff (92007)</li><li>Encinitas (92024)</li><li>Carlsbad (92009, 92008)</li>
    <li>La Jolla (92037)</li><li>Pacific Beach (92109)</li><li>Mira Mesa (92126)</li><li>Sorrento Valley (92121)</li>
    <li>Clairemont (92117)</li><li>Rancho Bernardo (92127, 92128)</li><li>Rancho Penasquitos (92129)</li><li>Poway (92064)</li>
  </ul>
</section>

<section>
  <div class="work-band abs"></div>
  <h2 class="work-title abs">Our Latest Work</h2>
  <article class="work-card abs" style="left:48px">
    <div class="photo" role="img" aria-label="Pool ladder descending into clear blue water" style="background:linear-gradient(180deg,#2c8fd6 0%,#56b4ea 45%,#b7e3f7 70%,#3ea6e0 100%)"></div>
    <h4>Swimming Pool</h4>
    <p>Lorem Ipsum is simply dummy text of the printing and typesetting industry. Lorem Ipsum has been the industry's standard dummy text</p>
  </article>
  <article class="work-card abs" style="left:259px">
    <div class="photo" role="img" aria-label="Two sun loungers under a white umbrella beside an infinity pool" style="background:linear-gradient(180deg,#3f8fd1 0%,#9acdee 45%,#c89a5a 68%,#2f9ad8 82%,#1a7fc4 100%)"></div>
    <h4>Spa Cleaning</h4>
    <p>Lorem Ipsum is simply dummy text of the printing and typesetting industry. Lorem Ipsum has been the industry's standard dummy text</p>
  </article>
  <article class="work-card abs" style="left:464px">
    <div class="photo" role="img" aria-label="New stone-edged pool with a raised spa" style="background:linear-gradient(180deg,#6b6660 0%,#b9b4aa 30%,#8fd3e6 55%,#cfd0c8 78%,#9fd9ea 100%)"></div>
    <h4>New Pool and Spa</h4>
    <p>Lorem Ipsum is simply dummy text of the printing and typesetting industry. Lorem Ipsum has been the industry's standard dummy text</p>
  </article>
</section>

<section>
  <h2 class="video-title abs">LATEST VIDEO</h2>
  <div class="video-rule abs"></div>
  <div class="video abs">
    <div class="frame" role="img" aria-label="Video still of a backyard pool with trees behind it"></div>
    <svg class="play" width="40" height="40" viewBox="0 0 40 40"><circle cx="20" cy="20" r="20" fill="rgba(0,0,0,.55)"/><path d="M16 12l12 8-12 8z" fill="#fff"/></svg>
    <div class="progress"></div>
    <div class="controls">
      <svg width="319" height="14" viewBox="0 0 319 14"><path d="M6 4l6 3-6 3z" fill="#ddd"/><rect x="20" y="4.5" width="4" height="5" fill="#ddd"/><path d="M24 4.5l4-2.5v10l-4-2.5z" fill="#ddd"/><text x="40" y="10" font-size="6" fill="#ddd" font-family="Barlow, sans-serif">0:00</text><rect x="296" y="4" width="7" height="6" fill="none" stroke="#ddd"/><rect x="308" y="4" width="6" height="6" fill="none" stroke="#ddd"/></svg>
    </div>
  </div>

  <h2 class="contact-title abs">Connect With Us</h2>
  <span class="field-label abs" style="top:940px">First Name (required)</span>
  <div class="field abs" style="top:950px"></div>
  <span class="field-label abs" style="top:976px">Email (required)</span>
  <div class="field abs" style="top:986px"></div>
  <span class="field-label abs" style="top:1012px">Phone number</span>
  <div class="field abs" style="top:1022px"></div>
  <span class="field-label abs" style="top:1048px">Message</span>
  <div class="field is-tall abs" style="top:1058px"></div>
  <div class="send abs">Send</div>
</section>

<footer class="site-footer abs"></footer>
<div class="copyright abs">Copyright © 2015 | Glimmerwave pool service</div>
<div class="social abs"><span></span><span></span><span></span></div>

</body>
</html>
```